Card for Real Estate Developer

We need a business card design for a Real Estate Development company based in Texas. We focus on retail, apartment and residential development. Our target is predominantly investors looking to us to place their money properly to achieve a significant return. On the other side we sell our services to large retailers as their preferred developer assisting them in locating, building and leasing their real estate.

Target Market(s)

Investors

Industry/Entity Type

Real Estate Development

Contact Information for Business Card

Would like to stay within the company color scheme, while keeping the design moderately simple.

Font styles to use
Other font styles liked:
• per attached document

Requirements
Must have
• Name
• Phone
• Email
• Website
• Logo Prominently Displayed
• Stay within the colors provided in the attached document

```html
<!DOCTYPE html>
<html lang="en">
<head>
<meta charset="utf-8">
<title>Harlow Development – Business Card</title>
<link href="https://fonts.googleapis.com/css2?family=Open+Sans:wght@400;600&display=swap" rel="stylesheet">
<style>
  :root {
    --backdrop: #8e8e8e;
    --card-black: #0c0c0c;
    --card-edge: #1a1a1a;
    --accent-blue: #74b6df;
    --text-white: #f2f2f2;
  }
  * { box-sizing: border-box; margin: 0; padding: 0; }
  html, body { width: 1200px; height: 900px; overflow: hidden; }
  body {
    background: var(--backdrop);
    font-family: "Open Sans", Arial, sans-serif;
    position: relative;
  }
  .card {
    position: absolute;
    left: 250px;
    width: 700px;
    height: 400px;
    background: radial-gradient(ellipse at 40% 35%, var(--card-edge), var(--card-black) 75%);
    box-shadow: 0 6px 18px rgba(0,0,0,.35);
    overflow: hidden;
  }
  .card-back { top: 35px; }
  .card-front { top: 465px; }

  /* brand name set as plain text */
  .brand {
    display: flex;
    align-items: center;
    gap: 16px;
    font-weight: 600;
    letter-spacing: 4px;
    text-transform: uppercase;
  }
  .brand-mark { width: 18px; height: 18px; flex: none; }
  .card-back .brand {
    position: absolute;
    inset: 0;
    justify-content: center;
    color: var(--text-white);
    font-size: 34px;
  }
  .card-back .brand-mark { background: var(--text-white); }
  .card-front .brand {
    position: absolute;
    left: 60px;
    top: 70px;
    color: var(--accent-blue);
    font-size: 24px;
    letter-spacing: 3px;
  }
  .card-front .brand-mark { background: var(--accent-blue); width: 14px; height: 14px; }

  .name-rule {
    position: absolute;
    left: 0;
    right: 0;
    top: 205px;
    display: flex;
    align-items: center;
    gap: 14px;
  }
  .name-rule .rule { height: 2px; background: var(--accent-blue); }
  .name-rule .rule-long { flex: 1; }
  .name-rule .rule-short { width: 36px; }
  .holder-name {
    color: var(--accent-blue);
    font-size: 24px;
    font-weight: 600;
    letter-spacing: .5px;
  }

  .contact-list {
    position: absolute;
    right: 50px;
    top: 255px;
    list-style: none;
    color: var(--text-white);
    font-size: 18px;
    line-height: 32px;
    text-align: right;
  }
  .contact-list li { display: flex; align-items: center; justify-content: flex-end; gap: 12px; }
  .contact-icon { width: 16px; height: 16px; fill: var(--accent-blue); }
</style>
</head>
<body>

  <section class="card card-back">
    <div class="brand"><span class="brand-mark"></span>Harlow Development</div>
  </section>

  <section class="card card-front">
    <div class="brand"><span class="brand-mark"></span>Harlow Development</div>

    <div class="name-rule">
      <span class="rule rule-long"></span>
      <span class="holder-name">Daniel Reyes</span>
      <span class="rule rule-short"></span>
    </div>

    <ul class="contact-list">
      <li>(044)-555-0142
        <svg class="contact-icon" viewBox="0 0 16 16" aria-hidden="true"><path d="M3.5 1.5l2.2 2.6-1.2 1.6c.9 2 2.6 3.8 4.8 4.8l1.6-1.2 2.6 2.2-1.3 2c-5.8-.6-9.9-4.7-10.5-10.5z"/></svg>
      </li>
      <li>info@harlowdev.com
        <svg class="contact-icon" viewBox="0 0 16 16" aria-hidden="true"><path d="M1 3.5h14v9H1z M1.8 4.3l6.2 4.6 6.2-4.6" fill="none" stroke="var(--accent-blue)" stroke-width="1.6"/></svg>
      </li>
      <li>www.harlowdev.com
        <svg class="contact-icon" viewBox="0 0 16 16" aria-hidden="true"><circle cx="8" cy="8" r="6.5" fill="none" stroke="var(--accent-blue)" stroke-width="1.5"/><path d="M1.5 8h13M8 1.5c-3 3.5-3 9.5 0 13M8 1.5c3 3.5 3 9.5 0 13" fill="none" stroke="var(--accent-blue)" stroke-width="1.2"/></svg>
      </li>
    </ul>
  </section>

</body>
</html>
```